New Business Card Design Project

2 sided business card required. I have attached some previous designs of items we have had made so you can see the logo etc. we Want the card to look professional and modern. for the final design upload for winning designer please note I need to be able to edit the names / phone numbers on the card design as I need to get them made for different staff.
Updates

extending time so designers can have time to submit

Target Market(s)

new customers

Industry/Entity Type

transport / earthmoving

Contact Information for Business Card

name, phone number email address

Requirements
Nice to have
• professional / impressive looking card (first impressions to customers count)
Should not have
• do not put our mobile number on the design use a generic number

```html
<!DOCTYPE html>
<html lang="en">
<head>
<meta charset="utf-8">
<title>Ridgeline Haulage – Business Card</title>
<link href="https://fonts.googleapis.com/css2?family=Arimo:wght@400;700&family=Open+Sans:wght@600&display=swap" rel="stylesheet">
<style>
  :root {
    --page: #ffffff;
    --card-black: #08090b;
    --copper: #d6975c;
    --ink: #111111;
    --white: #ffffff;
    --steel: #c9cbcf;
  }
  html, body {
    margin: 0;
    padding: 0;
    width: 826px;
    height: 1200px;
    overflow: hidden;
    background: var(--page);
    font-family: "Arimo", Arial, sans-serif;
  }
  .card {
    position: absolute;
    width: 636px;
    height: 362px;
    overflow: hidden;
    background: var(--card-black);
  }
  .card--front { left: 97px; top: 128px; }
  .card--back  { left: 94px; top: 643px; }

  /* Front */
  .front-photo {
    position: absolute;
    left: 0; top: 0;
    width: 636px; height: 307px;
    background:
      radial-gradient(ellipse 55% 60% at 50% 40%, #4a4b4e 0%, #1d1e20 55%, #050506 100%),
      #0a0a0b;
  }
  .front-photo::after {
    content: "";
    position: absolute;
    left: 0; right: 0; bottom: 0;
    height: 110px;
    background: linear-gradient(180deg, rgba(40,40,42,0) 0%, #3a3b3d 45%, #58595b 100%);
  }
  .front-name {
    position: absolute;
    left: 0; right: 0; top: 88px;
    text-align: center;
    font-weight: 700;
    font-size: 40px;
    letter-spacing: 1px;
    color: var(--steel);
    line-height: 1.1;
    z-index: 1;
  }
  .front-band {
    position: absolute;
    left: 0; bottom: 0;
    width: 636px; height: 55px;
    background: var(--copper);
    display: flex;
    align-items: center;
    justify-content: center;
  }
  .front-web {
    font-weight: 700;
    font-size: 20px;
    color: var(--ink);
  }

  /* Back */
  .back-name {
    position: absolute;
    left: 46px; top: 82px;
    width: 260px;
    text-align: center;
    font-weight: 700;
    font-size: 34px;
    line-height: 1.15;
    color: var(--steel);
  }
  .person {
    position: absolute;
    left: 386px; top: 66px;
  }
  .person-name {
    margin: 0;
    font-size: 23px;
    font-weight: 400;
    color: var(--copper);
    letter-spacing: 0.5px;
    line-height: 1;
  }
  .person-name strong { font-weight: 700; }
  .person-role {
    margin: 4px 0 0;
    font-size: 13px;
    color: var(--white);
  }
  .contact {
    position: absolute;
    left: 386px; top: 125px;
    margin: 0; padding: 0;
    list-style: none;
    font-family: "Open Sans", Arial, sans-serif;
    font-weight: 600;
    font-size: 9.5px;
    color: var(--white);
    line-height: 14px;
  }
  .contact li {
    display: flex;
    align-items: center;
    margin-bottom: 10px;
  }
  .contact svg {
    width: 14px; height: 14px;
    margin-right: 11px;
    flex-shrink: 0;
  }
  .back-band {
    position: absolute;
    left: 0; bottom: 0;
    width: 636px; height: 103px;
    background: var(--copper);
  }
  .services {
    position: absolute;
    top: 12px;
    margin: 0; padding: 0;
    list-style: none;
    font-size: 12.5px;
    line-height: 15.4px;
    color: var(--ink);
  }
  .services--one   { left: 24px; }
  .services--two   { left: 252px; }
  .services--three { left: 409px; }
</style>
</head>
<body>

<section class="card card--front">
  <div class="front-photo" role="img" aria-label="Photo of a road train with three tipper trailers on a gravel yard, set against a dark perforated metal backdrop"></div>
  <div class="front-name">Ridgeline Haulage</div>
  <div class="front-band">
    <span class="front-web">www.ridgeline-haul.com</span>
  </div>
</section>

<section class="card card--back">
  <div class="back-name">Ridgeline Haulage</div>

  <div class="person">
    <h1 class="person-name">SAM <strong>KELLER</strong></h1>
    <p class="person-role">Director</p>
  </div>

  <ul class="contact">
    <li>
      <svg viewBox="0 0 24 24" aria-hidden="true"><path fill="#d6975c" d="M6.6 10.8a15.1 15.1 0 0 0 6.6 6.6l2.2-2.2c.3-.3.7-.4 1-.2 1.1.4 2.3.6 3.6.6.6 0 1 .4 1 1V20c0 .6-.4 1-1 1A17 17 0 0 1 3 4c0-.6.4-1 1-1h3.5c.6 0 1 .4 1 1 0 1.3.2 2.5.6 3.6.1.3 0 .7-.2 1z"/></svg>
      <span>+18 2400 1350 2268<br>+18 2400 1350 4417</span>
    </li>
    <li>
      <svg viewBox="0 0 24 24" aria-hidden="true"><circle cx="12" cy="12" r="9" fill="none" stroke="#d6975c" stroke-width="2.2"/><path fill="#d6975c" d="M8 6l3 2-1 3-3 1-2-2zM13 13l4-1 2 3-3 4-2-1z"/></svg>
      <span>INFO@RIDGELINEHAUL.COM<br>WWW.RIDGELINE-HAUL.COM</span>
    </li>
    <li>
      <svg viewBox="0 0 24 24" aria-hidden="true"><path fill="none" stroke="#d6975c" stroke-width="2.2" d="M12 22s-6.5-7.3-6.5-12.2a6.5 6.5 0 0 1 13 0C18.5 14.7 12 22 12 22z"/><circle cx="12" cy="9.8" r="2.3" fill="#d6975c"/></svg>
      <span>YOUR CITY ADDRESS<br>STREET LOCATION, NY CITY, USA</span>
    </li>
  </ul>

  <div class="back-band">
    <ul class="services services--one">
      <li>Over size loads / Hot Shot Loads</li>
      <li>Heavy Vehicle Recovery Services</li>
      <li>Potable Water Deliveries</li>
      <li>Road Building/Maintenance</li>
    </ul>
    <ul class="services services--two">
      <li>Earthworks</li>
      <li>Sand &amp; Metal Supply</li>
      <li>&amp; Cartage.</li>
      <li>Road Train Tippers</li>
    </ul>
    <ul class="services services--three">
      <li>Road Train Tankers</li>
      <li>Road Train Flat Tops</li>
      <li>Drop Deck Trailers Mine Site</li>
      <li>accredited equipment &amp; Operators</li>
    </ul>
  </div>
</section>

</body>
</html>
```